Website for IT consulting Company

I need a website upgrade, the existing site content is ok, I would also like to add a testimonial page, the site should be something that is easy for us to update content. You use the content from www.kavnex.com as an example. I will also post update logo and artwork. I also need a contact form with some type of validation or captcha.

I added Coded to the Project

Please omit Address maps

Target Market(s)

small business, service oriented companies. We provide IT Consulting, support and mangement

Industry/Entity Type

Information Technology

Coding

Coded - Design and coding required

Number of Pages Required

1 page

Font styles to use
Serif
Sans Serif

Requirements
Must have
• Contain logo attached, and content from existing web site www.kavnex.com.
• Also need to update content easily, and be movable to different platforms.
• There is a catch phrase
• "Let us worry about your technology…” “ so you don’t have to!”
• Should be included.
Nice to have
• Testimonial page, Project page where we can post new and past projects and pictures
Should not have
• none

```html
<!DOCTYPE html>
<html lang="en">
<head>
<meta charset="utf-8">
<title>Kavnex Development Group — IT Solutions</title>
<link href="https://fonts.googleapis.com/css2?family=Maven+Pro:wght@400;500;700&family=Open+Sans:wght@400;600&family=Roboto:wght@400;500;700&display=swap" rel="stylesheet">
<style>
:root{
  --blue:#1a8fd6;
  --blue-deep:#1b5c9e;
  --blue-bar:#1d8ad2;
  --ink:#111;
  --text:#555;
  --pale:#eef4fb;
  --white:#fff;
  --hero-dark:#2d3035;
}
*{box-sizing:border-box;margin:0;padding:0}
html,body{width:1200px;height:2908px;overflow:hidden;background:var(--white)}
body{position:relative;font-family:"Open Sans",Arial,sans-serif;color:var(--text)}
.abs{position:absolute}
.heading{font-family:"Maven Pro",Arial,sans-serif;color:var(--ink);font-weight:400;display:flex;align-items:center;gap:10px}
.mark{display:inline-block;width:30px;height:30px;background:var(--blue);border-radius:4px}
.read-more{font-family:"Roboto",Arial,sans-serif;font-size:17px;color:var(--ink);text-decoration:underline;font-weight:500}
.more-arrow{font-family:"Roboto",Arial,sans-serif;font-weight:700;font-size:20px;color:var(--ink)}

/* hero */
.hero{left:0;top:0;width:1200px;height:640px;background:linear-gradient(120deg,#4a4f57 0%,#2d3035 45%,#5c6168 100%)}
.hero-photo{left:0;top:0;width:1200px;height:640px;background:radial-gradient(ellipse at 28% 55%,#8a7a70 0%,rgba(60,62,68,.4) 40%,rgba(45,48,53,0) 70%)}
.topbar{left:0;top:0;width:1200px;height:112px;background:rgba(30,32,36,.55);border-bottom:2px solid var(--blue)}
.logo{left:78px;top:30px;display:flex;align-items:center;gap:12px;font-family:"Maven Pro",sans-serif;font-weight:700;font-size:46px;color:#d9dde2;letter-spacing:1px}
.logo i{width:34px;height:34px;background:var(--blue);display:block}
.tagline{left:150px;top:84px;font-size:9px;color:#9fb6c9}
.menu{right:78px;top:38px;display:flex;align-items:center;gap:12px;color:#fff;font-family:"Roboto",sans-serif;font-size:22px}
.hero-title{right:78px;top:208px;text-align:right;font-family:"Roboto",sans-serif;font-weight:700;font-size:50px;line-height:67px;color:var(--blue)}
.hero-sub{right:78px;top:343px;font-family:"Roboto",sans-serif;font-size:23px;color:#fff}

/* about */
.about-title{left:0;width:1200px;top:680px;justify-content:center;font-size:42px}
.about-text{left:160px;width:880px;top:752px;text-align:center;font-size:13px;line-height:25px}
.about-more{left:0;width:1200px;top:832px;text-align:center}
.service{top:905px;width:330px}
.service .row{display:flex;align-items:center;gap:14px;margin-bottom:14px}
.service .ico{width:50px;height:50px;background:#cfe3f4;border-radius:6px;flex:none}
.service h3{font-family:"Roboto",sans-serif;font-weight:400;font-size:19px;line-height:24px;color:var(--blue)}
.service p{font-size:14px;line-height:22px}
.service .read-more{color:var(--blue);font-size:15px;display:block;margin-top:6px}
.service.first h3{color:var(--ink)}
.service.first .read-more{color:var(--ink)}
.chev{top:980px;font-size:36px;font-weight:700;color:var(--ink);font-family:"Roboto",sans-serif}

/* support band */
.band{left:0;top:1122px;width:1200px;height:800px;background:linear-gradient(180deg,#e9f1fa 0%,#f3f7fc 60%,#ffffff 100%)}
.photo-hacker{left:78px;top:1158px;width:522px;height:332px;background:linear-gradient(135deg,#0c1a3a 0%,#17357a 50%,#0a1630 100%)}
.support-title{right:78px;top:1148px;font-size:30px}
.support-text{right:78px;top:1200px;width:520px;text-align:right;font-size:14px;line-height:24px}
.support-list{left:662px;top:1286px;display:grid;grid-template-columns:262px 200px;row-gap:20px;font-family:"Roboto",sans-serif;font-size:16px;color:#222}
.support-list li{list-style:none;display:flex;align-items:center;gap:10px}
.support-list li::before{content:"";width:18px;height:18px;border-radius:50%;background:#5da7dd;display:block}
.out-title{left:78px;top:1545px;font-size:30px}
.out-text{left:78px;top:1596px;width:440px;font-size:14px;line-height:24px}
.out-more{left:78px;top:1726px}
.photo-team{left:600px;top:1552px;width:522px;height:333px;background:linear-gradient(120deg,#d8dde3 0%,#9aa3ad 45%,#3f78c0 80%,#c9d0d8 100%)}

/* testimonial */
.testi-title{left:0;width:1200px;top:1978px;justify-content:center;font-size:40px}
.testi-sub{left:0;width:1200px;top:2046px;text-align:center;font-size:14px}
.quote{left:210px;top:2089px;width:780px;height:126px;background:var(--blue);border-radius:12px;padding:26px 40px;color:#fff;font-size:14px;line-height:25px}
.quote-mark{left:222px;top:2060px;font-family:Georgia,serif;font-size:80px;color:#5fb1e6;line-height:1}
.client{left:302px;top:2222px;font-family:"Roboto",sans-serif;font-size:17px;color:var(--ink)}
.dots{left:540px;top:2262px;display:flex;gap:4px}
.dots i{width:15px;height:15px;border:2px solid var(--blue);display:block}
.dots i.on{background:var(--blue)}

/* newsletter */
.news{left:0;top:2343px;width:1200px;height:117px;background:var(--pale)}
.news-title{left:78px;top:2376px;font-size:40px}
.news-input{left:446px;top:2378px;width:394px;height:47px;background:#fff;border:1px solid #c9d3dd;padding:0 14px;display:flex;align-items:center;font-size:15px;color:#666}
.news-btn{left:840px;top:2378px;width:157px;height:47px;background:var(--blue);color:#fff;font-family:"Roboto",sans-serif;font-size:19px;display:flex;align-items:center;justify-content:center}

/* footer */
.footer{left:0;top:2460px;width:1200px;height:395px;background:linear-gradient(180deg,#1a5a9c 0%,#1b5fa4 100%)}
.foot-h{top:2508px;font-family:"Maven Pro",sans-serif;font-size:20px;font-weight:400;color:#fff}
.links{left:78px;top:2548px;list-style:none;color:#fff;font-size:14px;line-height:25px}
.field{left:442px;width:322px;border-bottom:1px solid #8fb3d8;color:#9fc0e0;font-size:14px;padding:0 0 8px 10px}
.send{left:442px;top:2760px;width:120px;height:40px;background:#fff;color:var(--blue-deep);font-family:"Roboto",sans-serif;font-size:18px;display:flex;align-items:center;justify-content:center;border-radius:3px}
.contact{left:816px;top:2548px;color:#dbe7f3;font-size:14px;line-height:24px}
.contact .item{display:flex;gap:18px;margin-bottom:20px}
.contact svg{flex:none;margin-top:4px}

/* bottom bar */
.bottom{left:0;top:2855px;width:1200px;height:53px;background:var(--blue-bar)}
.copy{left:78px;top:2871px;font-size:15px;color:#fff}
.copy b{color:#0a1f3a}
.social{top:2860px;width:42px;height:42px;border-radius:50%}
.social.fill{background:#fff}
.social.ring{border:2px solid #fff}
</style>
</head>
<body>

<div class="abs hero"></div>
<div class="abs hero-photo" role="img" aria-label="Photo of a smiling businesswoman typing on a laptop in a blurred office"></div>
<svg class="abs" style="left:0;top:540px" width="1200" height="100" viewBox="0 0 1200 100"><path d="M0 100 L0 62 Q80 40 180 38 L600 -10 L1200 100 Z" fill="#fff"/></svg>
<header class="abs topbar"></header>
<div class="abs logo"><i></i>KAVNEX</div>
<div class="abs tagline">Let us worry about your technology… so you don’t have to!</div>
<div class="abs menu">MENU
  <svg width="28" height="22" viewBox="0 0 28 22"><rect y="0" width="28" height="4" fill="#fff"/><rect y="9" width="28" height="4" fill="#fff"/><rect y="18" width="28" height="4" fill="#fff"/></svg>
</div>
<h1 class="abs hero-title">IT SOLUTIONS THAT WORK<br>FOR YOUR BUSINESS.</h1>
<p class="abs hero-sub">A full service technology company</p>

<h2 class="abs heading about-title"><i class="mark"></i>ABOUT US</h2>
<p class="abs about-text">Kavnex Development Group, Inc. was established in 1991. Our mission is helping businesses and individuals realize a Return on Investment by implementing today’s advanced technologies. As a small business we understand the importance of technology and personalized attention.Every member of our support team has worked with both large and small companies…</p>
<div class="abs about-more"><a class="read-more">READ MORE</a><span class="more-arrow"> »</span></div>

<div class="abs chev" style="left:30px">«</div>
<div class="abs chev" style="left:1150px">»</div>

<div class="abs service first" style="left:78px">
  <div class="row"><span class="ico" role="img" aria-label="Gear and hand icon"></span><h3>Managed IT Solutions</h3></div>
  <p>Our staff will design, service, administer and maintain your IT needs. We are well versed on all major operating system…</p>
  <a class="read-more">READ MORE »</a>
</div>
<div class="abs service" style="left:442px">
  <div class="row"><span class="ico" role="img" aria-label="Diagnostic screen icon"></span><h3>Remote Diagnostic and Support</h3></div>
  <p>Do you need a quick solution to a technical problem? With our live remote-assistance tool, a member of our support team…</p>
  <a class="read-more">READ MORE »</a>
</div>
<div class="abs service" style="left:806px">
  <div class="row"><span class="ico" role="img" aria-label="Server and monitor icon"></span><h3>IT Infrastructure Design and Installation</h3></div>
  <p>Do you have more than one site? Do you need remote access? We can design and implement LANS/WANS and VPN’s…</p>
  <a class="read-more">READ MORE »</a>
</div>

<section class="abs band"></section>
<div class="abs photo-hacker" role="img" aria-label="Photo of a man typing at a keyboard among glowing security labels"></div>
<h2 class="abs heading support-title"><i class="mark"></i>IT SUPPORT SOLUTIONS</h2>
<p class="abs support-text">Kavnex is a technology solution provider based in Houston, Texas.Kavnex has the experience, the tools, high-level technology solutions and training to power your business and your work force.</p>
<ul class="abs support-list">
  <li>Network Asministration</li><li>Wireless Network</li>
  <li>Antivirus Solution</li><li>Network cabling</li>
  <li>Network Security</li><li>Desktop Support</li>
</ul>

<h2 class="abs heading out-title"><i class="mark"></i>OUTSOURCING TECHNOLOGY</h2>
<p class="abs out-text">In today’s world, companies are expected to use technology to function and stay competitive. However, this aspect of business provides many challenges that most companies cannot solve on their own. Outsourcing technology provides solutions to almost every aspect of your business and can increase your profits.</p>
<div class="abs out-more"><a class="read-more">READ MORE</a><span class="more-arrow"> »</span></div>
<div class="abs photo-team" role="img" aria-label="Photo of two colleagues smiling at a computer monitor in an office"></div>

<h2 class="abs heading testi-title"><i class="mark"></i>TESTIMONIAL</h2>
<p class="abs testi-sub">What People Say About Hartwell &amp; Lane, P.C from Our Customer</p>
<div class="abs quote">“Lorem Ipsum is simply dummy text of the printing and typesetting industry. Lorem Ipsum has been the industry’s standard dummy text ever since the 1500s, when an unknown printer took a galley of type and scrambled it to make a type specimen book.”</div>
<svg class="abs" style="left:258px;top:2213px" width="30" height="24" viewBox="0 0 30 24"><path d="M0 0 H30 L4 24 Z" fill="#1a8fd6"/></svg>
<div class="abs quote-mark">“</div>
<div class="abs client">-Client Name</div>
<div class="abs dots"><i></i><i class="on"></i><i></i><i></i><i></i><i></i></div>

<section class="abs news"></section>
<h2 class="abs heading news-title"><i class="mark"></i>NEWSLETTER</h2>
<div class="abs news-input">Enter Email Id</div>
<div class="abs news-btn">SUBSCRIBE</div>

<footer class="abs footer"></footer>
<h4 class="abs foot-h" style="left:78px">USEFULL LINKS</h4>
<ul class="abs links"><li>Home</li><li>About</li><li>Services</li><li>Careers</li><li>Solution</li><li>Contact</li></ul>
<h4 class="abs foot-h" style="left:442px">QUICK CONTACT</h4>
<div class="abs field" style="top:2544px">Enter name</div>
<div class="abs field" style="top:2586px">Enter Email</div>
<div class="abs field" style="top:2628px">Enter Contact No.</div>
<div class="abs field" style="top:2670px;height:78px">Enter Message</div>
<div class="abs send">SEND</div>
<h4 class="abs foot-h" style="left:816px">CONTACT US</h4>
<div class="abs contact">
  <div class="item"><svg width="18" height="20" viewBox="0 0 18 20"><rect x="8" y="0" width="2" height="20" fill="#dbe7f3"/><rect x="0" y="3" width="18" height="5" fill="#dbe7f3"/><rect x="0" y="11" width="18" height="5" fill="#dbe7f3"/></svg>
    <div>Kavnex Development Group, Inc.<br>1450 Marlow Ave.<br>Houston, Texas 77019</div></div>
  <div class="item"><svg width="18" height="18" viewBox="0 0 24 24"><path d="M6.6 10.8a15 15 0 006.6 6.6l2.2-2.2a1 1 0 011-.25 11.4 11.4 0 003.6.57 1 1 0 011 1V20a1 1 0 01-1 1A17 17 0 013 4a1 1 0 011-1h3.5a1 1 0 011 1c0 1.25.2 2.45.57 3.57a1 1 0 01-.25 1z" fill="#dbe7f3"/></svg>
    <div>(713) 555-0148</div></div>
  <div class="item"><svg width="18" height="14" viewBox="0 0 18 14"><rect width="18" height="14" fill="#dbe7f3"/><path d="M0 0 L9 7 L18 0" stroke="#1b5c9e" stroke-width="1.6" fill="none"/></svg>
    <div>info@kavnex.com</div></div>
</div>

<div class="abs bottom"></div>
<p class="abs copy">© <b>Kavnex Development Group,Inc.</b> -2017 All Right Reserved</p>
<div class="abs social fill" style="left:976px" role="img" aria-label="Social profile link"></div>
<div class="abs social ring" style="left:1028px" role="img" aria-label="Social profile link"></div>
<div class="abs social ring" style="left:1080px" role="img" aria-label="Social profile link"></div>

</body>
</html>
```